TOLMANNER GRILL CONCEPT

Tolmanner is a new kebab concept from Germany that we want to adapt to the market, we are in a new market. black and white as on the picture. it takes colors in adequation with the stickers. the packaging that will be personalized in the bag

Target Market(s)

students, executives, office worker

Industry/Entity Type

Fast Food Chain

Font styles to use
Serif
Script

Colors

Designer to choose colors to be used in the design.

Requirements
Must have
• - TOLMANNER GRILL LOGO - 87 Rue des Quenouilles, 75011 Paris - "Seit 1971"

```html
<!DOCTYPE html>
<html lang="en">
<head>
<meta charset="utf-8">
<title>Tolmanner Grill — Stationery</title>
<link rel="stylesheet" href="https://fonts.googleapis.com/css2?family=Montserrat:wght@400;500&family=Roboto+Slab:wght@400&display=swap">
<style>
  :root {
    --bg: #8d8a86;
    --kraft: #c7ae7c;
    --kraft-dark: #b39a69;
    --paper: #ffffff;
    --ink: #111111;
    --ink-soft: #3a3a3a;
    --white: #ffffff;
  }
  * { box-sizing: border-box; margin: 0; padding: 0; }
  html, body { width: 1200px; height: 771px; overflow: hidden; }
  body { background: var(--bg); font-family: "Montserrat", sans-serif; color: var(--ink); position: relative; }

  .piece { position: absolute; box-shadow: 0 2px 6px rgba(0,0,0,.25); }

  .brand-disc {
    position: absolute; border-radius: 50%; background: var(--ink);
    display: flex; align-items: center; justify-content: center; text-align: center;
  }
  .brand-name {
    font-family: "Montserrat", sans-serif; font-weight: 400; color: var(--white);
    letter-spacing: .08em; line-height: 1.1;
  }

  /* envelope back */
  .envelope-back { left: 60px; top: 40px; width: 520px; height: 230px; background: var(--kraft); overflow: hidden; }
  .envelope-back svg { position: absolute; inset: 0; }
  .envelope-back .brand-disc { left: 24px; bottom: 20px; width: 90px; height: 90px; }
  .envelope-back .brand-name { font-size: 9px; }

  /* envelope front */
  .envelope-front { left: 60px; top: 300px; width: 520px; height: 230px; background: var(--kraft); }
  .envelope-front .return-address { position: absolute; left: 26px; top: 24px; font-size: 10px; font-weight: 500; }
  .envelope-front .brand-disc { right: 24px; top: 20px; width: 90px; height: 90px; }
  .envelope-front .brand-name { font-size: 9px; }

  /* letterhead */
  .letterhead { left: 620px; top: 40px; width: 520px; height: 250px; background: var(--paper); }
  .letterhead .brand-disc { left: 26px; top: 22px; width: 78px; height: 78px; }
  .letterhead .brand-name { font-size: 8px; }
  .letterhead .margin-rule { position: absolute; left: 128px; top: 14px; bottom: 14px; width: 1px; background: var(--ink); }
  .letter-body { position: absolute; left: 148px; top: 22px; right: 24px; font-family: "Roboto Slab", serif; font-size: 10.5px; line-height: 1.45; color: var(--ink-soft); }
  .letter-body p { margin-bottom: 10px; }

  /* business cards */
  .card-front { left: 620px; top: 330px; width: 260px; height: 160px; background: var(--paper); }
  .card-front .brand-disc { left: 65px; top: 15px; width: 130px; height: 130px; }
  .card-front .brand-name { font-size: 12px; }

  .card-back { left: 900px; top: 330px; width: 260px; height: 160px; background: var(--paper); }
  .card-back .holder-name { position: absolute; left: 20px; top: 26px; font-size: 22px; font-weight: 400; }
  .card-back .holder-role { position: absolute; left: 21px; top: 56px; font-size: 7.5px; color: var(--ink-soft); }
  .card-back .brand-disc { right: 18px; top: 18px; width: 56px; height: 56px; }
  .card-back .brand-name { font-size: 6px; }
  .card-back .card-address { position: absolute; left: 20px; bottom: 20px; font-size: 7px; font-weight: 500; }

  /* stickers and stamp */
  .sticker { position: absolute; border-radius: 50%; display: flex; align-items: center; justify-content: center; box-shadow: 0 2px 6px rgba(0,0,0,.25); }
  .sticker .brand-disc { position: static; width: 96px; height: 96px; }
  .sticker .brand-name { font-size: 9px; }
  .sticker-kraft { left: 90px; top: 570px; width: 120px; height: 120px; background: var(--kraft); }
  .sticker-white { left: 240px; top: 570px; width: 120px; height: 120px; background: var(--paper); }
  .stamp-face { left: 390px; top: 570px; width: 120px; height: 120px; background: #6e6054; border-radius: 8px; }
  .stamp-face .brand-disc { border: 4px solid #a9a9a9; }
</style>
</head>
<body>

  <section class="piece envelope-back" aria-label="Envelope back">
    <svg width="520" height="230" viewBox="0 0 520 230" aria-hidden="true">
      <polygon points="0,0 520,0 300,130 220,130" fill="var(--kraft-dark)"/>
      <polyline points="0,0 220,130 300,130 520,0" fill="none" stroke="#a58c5c" stroke-width="1"/>
    </svg>
    <div class="brand-disc"><span class="brand-name">TOLMANNER<br>GRILL</span></div>
  </section>

  <section class="piece letterhead" aria-label="Letterhead">
    <div class="brand-disc"><span class="brand-name">TOLMANNER<br>GRILL</span></div>
    <div class="margin-rule"></div>
    <div class="letter-body">
      <p>Dear Mr. Hartmann,</p>
      <p>Lorem ipsum dolor sit amet, consectetur adipiscing elit. Donec orci purus, luctus vitae dignissim eu, iaculis sed purus. Vivamus faucibus ipsum nec aliquet viverra.</p>
      <p>Vivamus et auctor mi. Fusce vel massa nulla. Phasellus nec eros mauris, et scelerisque orci.</p>
    </div>
  </section>

  <section class="piece envelope-front" aria-label="Envelope front">
    <p class="return-address">87 Rue des Quenouilles, 75011 Paris - "Since 1971"</p>
    <div class="brand-disc"><span class="brand-name">TOLMANNER<br>GRILL</span></div>
  </section>

  <section class="piece card-front" aria-label="Business card front">
    <div class="brand-disc"><span class="brand-name">TOLMANNER<br>GRILL</span></div>
  </section>

  <section class="piece card-back" aria-label="Business card back">
    <h1 class="holder-name">Jonas Weber</h1>
    <p class="holder-role">Co Founder &amp; CEO</p>
    <div class="brand-disc"><span class="brand-name">TOLMANNER<br>GRILL</span></div>
    <p class="card-address">87 Rue des Quenouilles, 75011 Paris - "Since 1971"</p>
  </section>

  <div class="sticker sticker-kraft" aria-label="Kraft sticker">
    <div class="brand-disc"><span class="brand-name">TOLMANNER<br>GRILL</span></div>
  </div>
  <div class="sticker sticker-white" aria-label="White sticker">
    <div class="brand-disc"><span class="brand-name">TOLMANNER<br>GRILL</span></div>
  </div>
  <div class="sticker stamp-face" aria-label="Rubber stamp face">
    <div class="brand-disc"><span class="brand-name">TOLMANNER<br>GRILL</span></div>
  </div>

</body>
</html>
```